Melissa Dorvan Personal Business Card

I like orange. It's would better if my card have an orange background
Address: 5820 Halvers Lane #417
San Jose
California
US
Tel: 4085172049

Industry/Entity Type

Business

```html
<!DOCTYPE html>
<html lang="en">
<head>
<meta charset="UTF-8">
<title>Melissa Dorvan – Business Card</title>
<link rel="stylesheet" href="https://fonts.googleapis.com/css2?family=Open+Sans:wght@500&family=Arimo:wght@400&display=swap">
<style>
  :root {
    --card-orange: #fd5c04;
    --frame-tint: rgba(255, 255, 255, 0.28);
    --text-white: #ffffff;
    --name-outline: #3a2a20;
  }
  html, body {
    margin: 0;
    padding: 0;
    width: 1200px;
    height: 686px;
    overflow: hidden;
    background: var(--card-orange);
  }
  .card {
    position: relative;
    width: 1200px;
    height: 686px;
    background: var(--card-orange);
    overflow: hidden;
  }
  .card__frames {
    position: absolute;
    inset: 0;
  }
  .card__frames polyline {
    fill: none;
    stroke: var(--frame-tint);
    stroke-linejoin: miter;
  }
  .card__identity {
    position: absolute;
    left: 595px;
    top: 348px;
    color: var(--text-white);
  }
  .card__name {
    margin: 0;
    font-family: "Open Sans", sans-serif;
    font-weight: 500;
    font-size: 84px;
    line-height: 1;
    letter-spacing: 0.5px;
    text-shadow:
      -1px -1px 0 var(--name-outline),
       1px -1px 0 var(--name-outline),
      -1px  1px 0 var(--name-outline),
       1px  1px 0 var(--name-outline);
  }
  .card__contact {
    margin: 22px 0 0 4px;
    font-family: "Arimo", sans-serif;
    font-style: normal;
    font-size: 22px;
    line-height: 28px;
    letter-spacing: 1.6px;
    word-spacing: 5px;
  }
  .card__contact span {
    display: block;
  }
</style>
</head>
<body>
  <main class="card">
    <svg class="card__frames" width="1200" height="686" viewBox="0 0 1200 686" aria-hidden="true">
      <polyline points="-20,66 447,66 447,621 -20,621" stroke-width="23"/>
      <polyline points="-20,138 369,138 369,710" stroke-width="19"/>
      <polyline points="-20,210 294,210 294,710" stroke-width="16"/>
      <polyline points="-20,280 227,280 227,710" stroke-width="13"/>
    </svg>

    <section class="card__identity">
      <h1 class="card__name">Melissa Dorvan</h1>
      <address class="card__contact">
        <span class="card__street">5820 Halvers Lane #417</span>
        <span class="card__city">San Jose, California US</span>
        <span class="card__phone">Tel: 4085172049</span>
      </address>
    </section>
  </main>
</body>
</html>
```